Dental Practice Billboard Design

We are a newer dental practice in need of a simple but appealing billboard for our growing dental practice to attract new patients. The practice is owned by husband and wife dentists and is family friendly in a small town in Kentucky. We try to be very friendly and caring to our patients. Would prefer a blue background for the billboard and our tooth logo to be prominent. We are partial to the Patua One font used in the image below but please feel free to tweak it as you deem necessary. The shape of the uppercase D and lowercase g are why we like that font, so fonts with a similarly shaped “D” and “g” would work as well. Please include our phone number (606) 847-3962. Please see our website Harlowfamilydentistry.com for more info on the practice if needed. Thank you! Looking forward to seeing your creation.
Updates

The dimensions will be 12ft x 24ft (3.6576m x 7.3152m). Apologies for not including this in the original prompt. Thank you all for your submissions.

Industry/Entity Type

Dental

Font styles to use
Other font styles liked:
• Patua One

Colors
0054AA
0677BA
7BADD7
CADEEF
E8F1F8
0094D4
00A9DD
6FCCEA
C7EBF8
E9F6FB
00AB8E
00BBA5
67D7C9
C6EFE9
E9F9F6
59FF00
82FF00
B8FF75
E3FFCB
F4FFEA

Requirements
Must have
• Phone number, website, Logo, Practice name “Harlow Family Dentistry”
Should not have
• A tagline or slogan

```html
<!DOCTYPE html>
<html lang="en">
<head>
<meta charset="utf-8">
<title>Harlow Family Dentistry Billboard</title>
<link href="https://fonts.googleapis.com/css2?family=Patua+One&family=Roboto:wght@700&display=swap" rel="stylesheet">
<style>
  :root {
    --page: #ececec;
    --white: #ffffff;
    --brand-blue: #1f55a5;
    --brand-green: #3aaa35;
    --green-light: #7cc242;
    --wave-top: #6db3d3;
    --wave-deep: #1594c4;
    --wave-dark: #1a7fb0;
    --photo-light: #e9ecef;
    --photo-mid: #c9c6c4;
    --photo-dark: #3a3a40;
  }
  * { box-sizing: border-box; margin: 0; padding: 0; }
  html, body { width: 1200px; height: 1200px; overflow: hidden; background: var(--page); }
  .billboard {
    position: absolute; left: 0; top: 300px;
    width: 1200px; height: 600px;
    background: linear-gradient(180deg, var(--white), #f3f5f7);
    overflow: hidden;
  }
  .wave { position: absolute; left: 0; top: 0; width: 1200px; height: 600px; }
  .brand {
    position: absolute; left: 80px; top: 70px;
    display: flex; align-items: center; gap: 36px;
  }
  .brand-dot {
    width: 150px; height: 150px; border-radius: 50%;
    background: var(--brand-green);
  }
  .brand-name {
    font-family: "Patua One", serif; color: var(--brand-blue);
    font-weight: 400; line-height: 1;
  }
  .brand-name .primary { display: block; font-size: 116px; }
  .brand-name .secondary { display: block; font-size: 50px; margin-top: 6px; }
  .phone {
    position: absolute; left: 80px; top: 318px;
    width: 560px; height: 96px; border-radius: 12px;
    background: linear-gradient(180deg, var(--green-light), var(--brand-green));
    display: flex; align-items: center; justify-content: center; gap: 22px;
    color: var(--white);
    font-family: "Roboto", sans-serif; font-weight: 700; font-size: 62px;
    white-space: nowrap;
  }
  .phone svg { width: 52px; height: 52px; flex: none; }
  .website {
    position: absolute; left: 80px; bottom: 52px;
    font-family: "Patua One", serif; font-size: 38px; color: var(--white);
    white-space: nowrap;
  }
  .team-photo {
    position: absolute; left: 740px; top: 120px; width: 460px; height: 480px;
    background: linear-gradient(180deg, var(--photo-mid) 0%, var(--photo-light) 45%, #d8dadd 75%, var(--photo-dark) 100%);
  }
</style>
</head>
<body>
  <main class="billboard">
    <svg class="wave" viewBox="0 0 1200 600" aria-hidden="true">
      <defs>
        <linearGradient id="waveFill" x1="0" y1="0" x2="1" y2="0">
          <stop offset="0" stop-color="#1594c4"/>
          <stop offset="1" stop-color="#1a7fb0"/>
        </linearGradient>
      </defs>
      <path d="M0 420 C 220 500 480 520 760 380 L 1200 300 L 1200 600 L 0 600 Z" fill="#6db3d3"/>
      <path d="M0 445 C 240 530 500 540 780 410 L 1200 330 L 1200 600 L 0 600 Z" fill="url(#waveFill)"/>
    </svg>

    <div class="brand">
      <div class="brand-dot"></div>
      <h1 class="brand-name">
        <span class="primary">Harlow</span>
        <span class="secondary">Family Dentistry</span>
      </h1>
    </div>

    <div class="phone">
      <svg viewBox="0 0 24 24" aria-hidden="true">
        <path fill="#fff" d="M6.6 10.8a15.1 15.1 0 0 0 6.6 6.6l2.2-2.2c.3-.3.7-.4 1-.2 1.1.4 2.3.6 3.6.6.6 0 1 .4 1 1V20c0 .6-.4 1-1 1A17 17 0 0 1 3 4c0-.6.4-1 1-1h3.5c.6 0 1 .4 1 1 0 1.3.2 2.5.6 3.6.1.3 0 .7-.2 1z"/>
        <path fill="none" stroke="#fff" stroke-width="1.5" stroke-linecap="round" d="M15 3.5a6 6 0 0 1 5.5 5.5M15 6.5a3 3 0 0 1 2.5 2.5"/>
      </svg>
      <span>(606) 847-3962</span>
    </div>

    <p class="website">www.HarlowFamilyDentistry.com</p>

    <div class="team-photo" role="img" aria-label="Photo of the two smiling dentists, a woman and a man in white coats over dark scrubs"></div>
  </main>
</body>
</html>
```